Lumavorne Business Card Design

I need a business card design for a new Business, that is focused on Custom Made Designer Furniture. that is aimed at the mid to high end markets. I would like a card that would in some way portray what I do for my clients in the way we are able to make any idea a reality and also work within a set budget to meet their requirements.
I like quite contemporary colours and styling and I want the final design to communicate a Contemporary and Professional image.

Target Market(s)

mid to high end market

Industry/Entity Type

Business

Contact Information for Business Card

Lumavorne
Harold Brenning
82 Wendle Ave, Tarrow, Auckland, New Zealand 0927.

Requirements
Nice to have
• I would also like to utilize the spot gloss or raised print on my cards

```html
<!DOCTYPE html>
<html lang="en">
<head>
<meta charset="utf-8">
<title>Lumavorne Business Card</title>
<link rel="stylesheet" href="https://fonts.googleapis.com/css2?family=PT+Sans&family=Quicksand:wght@500&display=swap">
<style>
  :root {
    --wood-light: #f2c98a;
    --wood-mid: #e8b26a;
    --wood-deep: #d99a4e;
    --ink: #111111;
    --violet: #8a00ff;
    --white: #ffffff;
  }
  html, body {
    margin: 0;
    padding: 0;
    overflow: hidden;
    background: #e6e6e6;
  }
  .card {
    position: relative;
    width: 1200px;
    height: 733px;
    overflow: hidden;
    font-family: "PT Sans", sans-serif;
  }
  .wood-surface {
    position: absolute;
    inset: 0;
    background: linear-gradient(178deg, var(--wood-light) 0%, var(--wood-mid) 35%, var(--wood-light) 60%, var(--wood-deep) 100%);
  }
  .chair-sketch {
    position: absolute;
    left: 850px;
    top: 54px;
    width: 342px;
    height: 679px;
    background: linear-gradient(180deg, rgba(255,255,255,0.22), rgba(255,255,255,0.12));
  }
  .brand-mark {
    position: absolute;
    left: 79px;
    top: 49px;
    width: 192px;
    height: 192px;
    border-radius: 50%;
    background: var(--ink);
    display: flex;
    align-items: center;
    justify-content: center;
  }
  .brand-name {
    color: var(--white);
    font-size: 30px;
    font-family: "PT Sans", sans-serif;
  }
  .divider {
    position: absolute;
    left: 309px;
    top: 59px;
    width: 3px;
    height: 158px;
    background: var(--ink);
  }
  .owner-name {
    position: absolute;
    left: 343px;
    top: 100px;
    margin: 0;
    font-weight: 400;
    font-size: 57px;
    line-height: 1;
    color: var(--ink);
  }
  .tagline-band {
    position: absolute;
    left: 0;
    top: 381px;
    width: 800px;
    height: 117px;
    background: var(--violet);
  }
  .tagline {
    position: absolute;
    left: 78px;
    top: 33px;
    margin: 0;
    font-family: "Quicksand", sans-serif;
    font-weight: 500;
    font-size: 38px;
    line-height: 1.2;
    letter-spacing: 0.5px;
    color: var(--white);
  }
  .address {
    position: absolute;
    left: 97px;
    top: 673px;
    margin: 0;
    font-size: 20px;
    color: var(--white);
    font-style: normal;
  }
</style>
</head>
<body>
  <main class="card">
    <div class="wood-surface" role="img" aria-label="Photograph of light pine wood grain with knots"></div>
    <div class="chair-sketch" role="img" aria-label="White line drawing of a chair back and seat"></div>

    <div class="brand-mark"><span class="brand-name">Lumavorne</span></div>
    <div class="divider"></div>
    <h1 class="owner-name">Harold Brenning</h1>

    <div class="tagline-band">
      <p class="tagline">Custom Made Designer Furniture</p>
    </div>

    <address class="address">82 Wendle Ave, Tarrow, Auckland, New Zealand 0927</address>
  </main>
</body>
</html>
```